METAL FABRICATION BUSINESS CARD

** I will be ending the project and picking design early. This Friday October 3rd at 7am MST if not sooner**
ONE SIDED BUSINESS CARD ONLY. AND LOGO SIZE TO BE DOMINANT so it stands out.
Looking for a black background and will be doing raised chrome/silver font on the business cards. Looking to have the following on the front of the business card. Company logo is uploaded in files.
Company logo
*Compartment Doors
*Roof Radius Metal
*J-Wrap Metal Skirting
*S-Lock Beltline Molding
*Pre-Bent Molding
and more...
Owen Baskell 406.529.1847 info@Trelvo-Works.com
Updates
One sided business card only please. Also logo size should be dominant and sized bigger
Contact Information for Business Card
Black background, Text will be raised chrome/silver, and corners will be rounded.

```html
<!DOCTYPE html>
<html lang="en">
<head>
<meta charset="utf-8">
<title>Trelvo-Works Business Card Options</title>
<link href="https://fonts.googleapis.com/css2?family=Lato:wght@400;700;900&display=swap" rel="stylesheet">
<style>
  :root {
    --page-bg: #050505;
    --card-dark: #16191c;
    --card-dark-2: #0d0f11;
    --silver-light: #f1f2f3;
    --silver-mid: #b9bcc0;
    --silver-dark: #6c7075;
    --text-silver: #d3d6d9;
    --text-soft: #c4c7ca;
    --text-on-silver: #1a1c1f;
    --label: #ffffff;
  }
  * { margin: 0; padding: 0; box-sizing: border-box; }
  html, body { width: 1200px; height: 878px; overflow: hidden; background: var(--page-bg); }
  body { font-family: "Lato", sans-serif; position: relative; }

  .option { position: absolute; top: 250px; width: 560px; }
  .option--one { left: 27px; }
  .option--two { left: 613px; }

  .option__label {
    text-align: center; color: var(--label);
    font-size: 22px; font-weight: 400; letter-spacing: 1px;
    margin-bottom: 24px;
  }

  .card {
    position: relative; width: 560px; height: 321px;
    border-radius: 18px; overflow: hidden;
    background: linear-gradient(160deg, var(--card-dark), var(--card-dark-2));
  }
  .card__shapes { position: absolute; inset: 0; width: 100%; height: 100%; }

  .brand {
    position: absolute; font-weight: 900; color: var(--text-silver);
    font-size: 64px; line-height: 1; letter-spacing: -1px; white-space: nowrap;
  }
  .card--one .brand { left: 50px; top: 100px; }
  .card--two .brand { left: 0; right: 0; top: 70px; text-align: center; }

  .contact { position: absolute; color: var(--text-soft); }
  .contact__name { font-size: 22px; font-weight: 900; color: var(--text-silver); letter-spacing: 0.5px; margin-bottom: 4px; }
  .contact__line { display: flex; align-items: center; gap: 8px; font-size: 16px; line-height: 22px; }
  .contact__line svg { width: 11px; height: 11px; fill: var(--text-soft); flex: none; }
  .card--one .contact { left: 52px; top: 218px; }
  .card--two .contact { left: 42px; top: 203px; }
  .card--two .contact__phone { font-weight: 700; }

  .services { position: absolute; list-style: none; }
  .services li { line-height: 19px; }
  .services li.bullet::before { content: "•"; display: inline-block; width: 14px; }
  .services li.more { padding-left: 14px; }
  .card--one .services { left: 320px; top: 178px; font-size: 14px; color: var(--text-soft); }
  .card--two .services { left: 314px; top: 180px; font-size: 14px; font-weight: 700; color: var(--text-on-silver); }
  .card--two .services li.more { padding-left: 0; font-weight: 400; }
</style>
</head>
<body>

<section class="option option--one">
  <h2 class="option__label">FRONT &amp; BACK 01</h2>
  <div class="card card--one">
    <svg class="card__shapes" viewBox="0 0 560 321" preserveAspectRatio="none" aria-hidden="true">
      <defs>
        <linearGradient id="chrome-a" x1="0" y1="0" x2="1" y2="0">
          <stop offset="0" stop-color="#6c7075"/>
          <stop offset="0.35" stop-color="#f1f2f3"/>
          <stop offset="0.7" stop-color="#9a9ea2"/>
          <stop offset="1" stop-color="#e4e5e6"/>
        </linearGradient>
      </defs>
      <path d="M0 0 H226 C110 30 20 110 0 212 Z" fill="url(#chrome-a)"/>
      <path d="M560 212 C545 270 505 310 442 321 H560 Z" fill="url(#chrome-a)"/>
    </svg>
    <div class="brand">Trelvo-Works</div>
    <div class="contact">
      <p class="contact__name">Owen Baskell</p>
      <p class="contact__line"><svg viewBox="0 0 12 12"><path d="M2.5 0.5l2 2.4-1.2 1.4c.7 1.6 2 2.9 3.6 3.6l1.4-1.2 2.4 2-1.2 2.3C5 10.4 1.6 7 .2 1.7z"/></svg>406.529.1847</p>
      <p class="contact__line"><svg viewBox="0 0 12 12"><path d="M0 2h12v8H0z M0 2l6 4.5L12 2" /></svg>info@Trelvo-Works.com</p>
    </div>
    <ul class="services">
      <li class="bullet">Compartment Doors</li>
      <li class="bullet">Roof Radius Metal</li>
      <li class="bullet">J-Wrap Metal Skirting</li>
      <li class="bullet">S-Lock Beltline Molding</li>
      <li class="bullet">Pre-Bent Molding</li>
      <li class="more">and more...</li>
    </ul>
  </div>
</section>

<section class="option option--two">
  <h2 class="option__label">FRONT &amp; BACK 02</h2>
  <div class="card card--two">
    <svg class="card__shapes" viewBox="0 0 560 321" preserveAspectRatio="none" aria-hidden="true">
      <defs>
        <linearGradient id="chrome-b" x1="0" y1="0" x2="0" y2="1">
          <stop offset="0" stop-color="#dcdee0"/>
          <stop offset="0.3" stop-color="#9fa3a7"/>
          <stop offset="0.6" stop-color="#f1f2f3"/>
          <stop offset="1" stop-color="#8b8f93"/>
        </linearGradient>
      </defs>
      <path d="M0 162 H36 L0 242 Z" fill="url(#chrome-b)"/>
      <path d="M296 162 H560 V321 H231 Z" fill="url(#chrome-b)"/>
    </svg>
    <div class="brand">Trelvo-Works</div>
    <div class="contact">
      <p class="contact__name">Owen Baskell</p>
      <p class="contact__line contact__phone"><svg viewBox="0 0 12 12"><path d="M2.5 0.5l2 2.4-1.2 1.4c.7 1.6 2 2.9 3.6 3.6l1.4-1.2 2.4 2-1.2 2.3C5 10.4 1.6 7 .2 1.7z"/></svg>406.529.1847</p>
      <p class="contact__line"><svg viewBox="0 0 12 12"><path d="M0 2h12v8H0z M0 2l6 4.5L12 2"/></svg>info@Trelvo-Works.com</p>
    </div>
    <ul class="services">
      <li class="bullet">COMPARTMENT DOORS</li>
      <li class="bullet">ROOF RADIUS METAL</li>
      <li class="bullet">J-WRAP METAL SKIRTING</li>
      <li class="bullet">S-LOCK BELTLINE MOLDING</li>
      <li class="bullet">PRE-BENT MOLDING</li>
      <li class="more">AND MORE...</li>
    </ul>
  </div>
</section>

</body>
</html>
```